Web design for a crypto donation landing page for wildlife protection projects

We are developing the landing page for the presale of a web3 project, which will collect cryptos to send them to wildlife protection projects.
Here some website we like:
https://www.tidegroveaccord.fr/
https://qelvo.io/
https://www.mossvalen.io/
please, use the wireframe to know what blocks we want but we accept different template.
If possible, do the design on figma. Use 1 or 2 fonts max. Used green, blue and white, no more. Make a consistent system design by using the same font size for H1, H2, H3... and the same colors everywhere.

```html
<!DOCTYPE html>
<html lang="fr">
<head>
<meta charset="utf-8">
<title>Verdalis – Protégeons la nature ensemble</title>
<link rel="stylesheet" href="https://fonts.googleapis.com/css2?family=Poppins:wght@400;500;600;700&display=swap">
<style>
:root{
  --blue-deep:#1b1470;
  --blue:#2a1fa0;
  --green:#5cb82a;
  --white:#ffffff;
  --ink:#1f1a5e;
  --muted:#55567a;
  --line:#e3e4ef;
}
*{box-sizing:border-box;margin:0;padding:0}
html,body{width:1200px;height:3896px;overflow:hidden}
body{font-family:'Poppins',sans-serif;color:var(--ink);background:var(--white);position:relative}
h2{font-size:40px;font-weight:700;line-height:1.2}
.section{position:absolute;left:0;width:1200px}
/* hero */
.hero{top:0;height:580px;color:var(--white);
  background:radial-gradient(circle at 75% 55%,#4a3fd6 0,#2a1fa0 40%,#160f5c 100%)}
.hero-photo{position:absolute;inset:0;background:linear-gradient(120deg,rgba(22,15,92,0) 40%,rgba(90,70,160,.45) 75%,rgba(120,80,60,.35) 100%)}
.nav{position:absolute;top:24px;left:110px;right:110px;display:flex;justify-content:space-between;align-items:center}
.brand{display:flex;align-items:center;gap:10px;font-weight:700;font-size:24px;color:var(--white)}
.brand-dot{width:34px;height:34px;border-radius:50%;background:var(--green)}
.burger span{display:block;width:34px;height:3px;background:var(--white);margin:7px 0;border-radius:2px}
.hero-copy{position:absolute;left:110px;top:165px;width:640px}
.hero-copy h1{font-size:38px;font-weight:700;line-height:1.2;margin-bottom:24px;white-space:nowrap}
.hero-copy .lead{font-size:19px;font-weight:600;line-height:1.4;margin-bottom:18px;width:600px}
.hero-copy p{font-size:14px;line-height:1.55}
.partners{display:flex;gap:40px;margin-top:36px;align-items:center}
.partner{width:110px;height:26px;border-radius:13px;background:rgba(255,255,255,.55)}
.buy-card{position:absolute;left:790px;top:180px;width:300px;padding:26px 26px;background:var(--white);border-radius:22px;color:var(--ink);text-align:center;box-shadow:0 20px 40px rgba(0,0,0,.25)}
.buy-card h3{font-size:19px;font-weight:600;margin-bottom:22px}
.qty{display:flex;justify-content:center;align-items:center;gap:26px;border:1px solid var(--line);border-radius:8px;height:44px;margin-bottom:16px;font-weight:600;font-size:18px}
.qty span{color:var(--green);font-size:22px}
.rate{font-size:15px;font-weight:600;color:var(--blue);margin-bottom:24px}
.btn{display:inline-block;background:var(--green);color:var(--white);font-weight:600;font-size:15px;padding:12px 40px;border-radius:6px}
/* how */
.how{top:580px;height:690px;text-align:center}
.how h2{color:var(--blue);width:760px;margin:76px auto 46px}
.cards{display:flex;justify-content:center;gap:40px}
.card{width:310px;height:370px;padding:24px 26px;border-radius:22px;background:var(--white);box-shadow:0 8px 30px rgba(40,30,120,.14)}
.icon{width:110px;height:110px;border-radius:50%;background:var(--blue);border:8px solid #d8d6f5;margin:0 auto 18px;display:flex;align-items:center;justify-content:center}
.card h3{font-size:20px;font-weight:700;color:var(--blue);line-height:1.3;margin-bottom:10px}
.card p{font-size:14px;color:var(--muted);line-height:1.45}
/* community */
.community{top:1270px;height:470px;color:var(--white);background:linear-gradient(90deg,#1f168a,#3526c4)}
.community-copy{position:absolute;left:110px;top:70px;width:720px}
.community h2{margin-bottom:30px;font-size:38px}
.community .lead{font-size:19px;font-weight:600;line-height:1.4;margin-bottom:18px}
.community p{font-size:14px;margin-bottom:14px}
.checks li{list-style:none;display:flex;gap:12px;align-items:center;font-size:14px;margin-bottom:8px}
.tick{width:18px;height:18px;border:2px solid var(--green);border-radius:3px;display:flex;align-items:center;justify-content:center}
.socials{position:absolute;left:880px;top:210px;display:flex;gap:36px}
.social{width:76px;height:76px;border-radius:14px;background:var(--green)}
/* roadmap */
.roadmap{top:1740px;height:600px;text-align:center}
.roadmap h2{color:var(--green);margin-top:90px}
.arrows{display:flex;justify-content:center;gap:60px;margin-top:16px;font-size:28px;font-weight:700}
.arrows .next{color:var(--green)}
.track{position:absolute;left:100px;right:0;top:380px;height:50px;background:var(--green);border-top:10px solid var(--blue-deep);border-bottom:10px solid var(--blue-deep)}
.track::after{content:"";position:absolute;left:0;right:0;top:13px;border-top:6px dashed var(--white)}
.quarter{position:absolute;text-align:left;font-size:14px;line-height:1.8}
.quarter b{display:block;font-size:14px;font-weight:700;margin-bottom:4px}
.quarter li{list-style:none;padding-left:18px;position:relative}
.quarter li::before{content:"";position:absolute;left:0;top:7px;border-left:8px solid var(--green);border-top:5px solid transparent;border-bottom:5px solid transparent}
/* faqs */
.faqs{top:2340px;height:610px;text-align:center;color:var(--white);background:radial-gradient(circle at 80% 40%,#3a2dc8,#1b1470 75%)}
.faqs h2{margin:100px 0 40px}
.faq{width:700px;height:42px;margin:0 auto 18px;background:var(--white);border-radius:8px;display:flex;align-items:center;padding:0 20px;color:var(--ink);font-size:14px}
.faq b{color:var(--green);font-weight:600;margin-right:10px}
.faq svg{margin-left:auto}
/* team */
.team{top:2950px;height:610px;text-align:center}
.team h2{color:var(--green);margin:70px 0 50px}
.members{display:flex;justify-content:center;gap:50px}
.member{width:250px;height:300px;border-radius:18px;background:var(--white);box-shadow:0 8px 30px rgba(40,30,120,.14);padding:18px}
.portrait{height:200px;border-radius:10px;background:linear-gradient(160deg,#c9cbd4,#8b8fa6)}
.member h3{color:var(--green);font-size:16px;font-weight:600;margin-top:18px}
.member p{font-size:13px;color:var(--muted)}
/* footer */
.footer{top:3560px;height:336px;color:var(--white);background:linear-gradient(90deg,#1f168a,#3526c4)}
.foot-brand{position:absolute;left:110px;top:46px;width:260px}
.foot-brand .brand{font-size:22px;margin-bottom:14px}
.foot-brand p{font-size:14px;line-height:1.5}
.foot-col{position:absolute;top:50px;font-size:14px;line-height:1.9}
.foot-col h4{font-size:17px;font-weight:600;margin-bottom:6px}
.foot-col .row{display:flex;gap:10px;align-items:flex-start;line-height:1.5;margin-bottom:10px}
.foot-col .sq{width:14px;height:14px;border-radius:3px;background:var(--white);flex:none;margin-top:3px}
.copy{position:absolute;left:110px;top:296px;font-size:13px}
</style>
</head>
<body>

<header class="section hero">
  <div class="hero-photo" role="img" aria-label="Photo d'ambiance nature et cryptomonnaie en fond, teintes bleu nuit"></div>
  <nav class="nav">
    <div class="brand"><span class="brand-dot"></span>Verdalis</div>
    <div class="burger"><span></span><span></span><span></span></div>
  </nav>
  <div class="hero-copy">
    <h1>Protégeons la nature ensemble</h1>
    <p class="lead">Faites un don de tokens et aidez à protéger la faune et flore.</p>
    <p>Notre plateforme vous permet d'ajouter des tokens de votre choix pour les donner à un projet de protection de la nature. Votre contribution aidera à financer des actions concrètes pour préserver l'environnement.</p>
    <div class="partners"><span class="partner"></span><span class="partner"></span><span class="partner"></span></div>
  </div>
  <div class="buy-card">
    <h3>Acheter des token</h3>
    <div class="qty"><span>−</span>12<span>+</span></div>
    <div class="rate">12 token = 30 €</div>
    <span class="btn">Acheter</span>
  </div>
</header>

<section class="section how">
  <h2>Comment protéger la nature avec des tokens Verdalis ?</h2>
  <div class="cards">
    <div class="card">
      <div class="icon"><svg width="46" height="46" viewBox="0 0 46 46" fill="none" stroke="#fff" stroke-width="3"><circle cx="23" cy="23" r="18"/><circle cx="23" cy="23" r="10"/></svg></div>
      <h3>Achetez des tokens Verdalis</h3>
      <p>Les tokens sont des actifs numériques qui peuvent être utilisés pour financer des projets des associations</p>
    </div>
    <div class="card">
      <div class="icon"><svg width="46" height="46" viewBox="0 0 46 46" fill="none" stroke="#fff" stroke-width="3"><rect x="8" y="18" width="30" height="22" rx="3"/><path d="M16 24l5 5 9-11"/><path d="M14 18V8h18v10"/></svg></div>
      <h3>Votez pour un projet</h3>
      <p>Vous pouvez voter pour un projet de votre choix. Les projets sont proposés par des associations et des ONG qui travaillent pour la protection de la nature.</p>
    </div>
    <div class="card">
      <div class="icon"><svg width="46" height="46" viewBox="0 0 46 46" fill="none" stroke="#fff" stroke-width="3"><path d="M6 30c8 0 10-6 18-6h8"/><path d="M6 38h20l14-10"/><circle cx="32" cy="12" r="6"/></svg></div>
      <h3>L'association choisit reçoit l'argent</h3>
      <p>Le projet qui a reçu le plus de votes reçoit les tokens. L'association pourra utiliser cet argent pour financer ses actions concrètes pour protéger la nature.</p>
    </div>
  </div>
</section>

<section class="section community">
  <div class="community-copy">
    <h2>Rejoignez la communauté pour soutenir la protection de la nature</h2>
    <p class="lead">La nature est en danger, nous devons agir ensemble. Rejoignez la communauté pour soutenir la protection de la nature.</p>
    <p>En rejoignant la communauté, vous pourrez :</p>
    <ul class="checks">
      <li><span class="tick"><svg width="10" height="10" viewBox="0 0 10 10" fill="none" stroke="#5cb82a" stroke-width="2"><path d="M1 5l3 3 5-7"/></svg></span>Suivre les projets des associations qui travaillent pour la protection de la nature.</li>
      <li><span class="tick"><svg width="10" height="10" viewBox="0 0 10 10" fill="none" stroke="#5cb82a" stroke-width="2"><path d="M1 5l3 3 5-7"/></svg></span>Voter pour le projet de votre choix et aider à financer ses actions concrètes.</li>
      <li><span class="tick"><svg width="10" height="10" viewBox="0 0 10 10" fill="none" stroke="#5cb82a" stroke-width="2"><path d="M1 5l3 3 5-7"/></svg></span>Être informé des dernières actualités sur la protection de la nature.</li>
    </ul>
  </div>
  <div class="socials"><span class="social" aria-label="Chatterly"></span><span class="social" aria-label="Chirpnet"></span></div>
</section>

<section class="section roadmap">
  <h2>Roadmap</h2>
  <div class="arrows"><span>←</span><span class="next">→</span></div>
  <div class="quarter" style="left:150px;top:228px"><b>Q1. 2024</b><ul><li>Site internet &amp; réseaux sociaux</li><li>Marketing &amp; Développement du smart</li><li>Juridique et Pré vente n°1</li><li>Développement du smart contract tesnet</li></ul></div>
  <div class="quarter" style="left:610px;top:228px"><b>Q3. 2024</b><ul><li>Site internet &amp; réseaux sociaux</li><li>Marketing &amp; Développement du smart</li><li>Juridique et Pré vente n°1</li><li>Développement du smart contract tesnet</li></ul></div>
  <div class="track"></div>
  <div class="quarter" style="left:390px;top:460px"><b>Q2. 2024</b><ul><li>Site internet &amp; réseaux sociaux</li><li>Marketing &amp; Développement du smart</li></ul></div>
  <div class="quarter" style="left:850px;top:460px"><b>Q4. 2024</b><ul><li>Site internet &amp; réseaux sociaux</li><li>Marketing &amp; Développement</li></ul></div>
</section>

<section class="section faqs">
  <h2>Faqs</h2>
  <div class="faq"><b>Q1.</b>Lorem ipsum dolor sit amet, consectetur adipiscing II<svg width="14" height="10" viewBox="0 0 14 10" fill="none" stroke="#1f1a5e" stroke-width="2"><path d="M2 2l5 5 5-5"/></svg></div>
  <div class="faq"><b>Q2.</b>Lorem ipsum dolor sit amet, consectetur adipiscing II<svg width="14" height="10" viewBox="0 0 14 10" fill="none" stroke="#1f1a5e" stroke-width="2"><path d="M2 2l5 5 5-5"/></svg></div>
  <div class="faq"><b>Q3.</b>Lorem ipsum dolor sit amet, consectetur adipiscing II<svg width="14" height="10" viewBox="0 0 14 10" fill="none" stroke="#1f1a5e" stroke-width="2"><path d="M2 2l5 5 5-5"/></svg></div>
  <div class="faq"><b>Q4.</b>Lorem ipsum dolor sit amet, consectetur adipiscing II<svg width="14" height="10" viewBox="0 0 14 10" fill="none" stroke="#1f1a5e" stroke-width="2"><path d="M2 2l5 5 5-5"/></svg></div>
  <div class="faq"><b>Q5.</b>Lorem ipsum dolor sit amet, consectetur adipiscing II<svg width="14" height="10" viewBox="0 0 14 10" fill="none" stroke="#1f1a5e" stroke-width="2"><path d="M2 2l5 5 5-5"/></svg></div>
  <div class="faq"><b>Q6.</b>Lorem ipsum dolor sit amet, consectetur adipiscing II<svg width="14" height="10" viewBox="0 0 14 10" fill="none" stroke="#1f1a5e" stroke-width="2"><path d="M2 2l5 5 5-5"/></svg></div>
</section>

<section class="section team">
  <h2>Team</h2>
  <div class="members">
    <div class="member"><div class="portrait" role="img" aria-label="Portrait du fondateur"></div><h3>Marchetti Julien</h3><p>Fondateur</p></div>
    <div class="member"><div class="portrait" role="img" aria-label="Portrait de la développeuse blockchain"></div><h3>Lemaire Sophie</h3><p>Developpeuse blockchain</p></div>
    <div class="member"><div class="portrait" role="img" aria-label="Portrait de la développeuse front-end"></div><h3>Dorval Inès</h3><p>Développeur front-end</p></div>
  </div>
</section>

<footer class="section footer">
  <div class="foot-brand">
    <div class="brand"><span class="brand-dot"></span>Verdalis</div>
    <p>Notre plateforme vous permet d'ajouter des tokens de votre choix pour les donner à un projet de protection de la nature.</p>
  </div>
  <div class="foot-col" style="left:480px"><h4>Quick Links</h4>Home<br>About<br>Road map<br>Team<br>Contact</div>
  <div class="foot-col" style="left:660px;width:240px">
    <h4>Contact Us</h4>
    <div class="row"><svg width="14" height="18" viewBox="0 0 14 18" fill="#fff"><path d="M7 0a7 7 0 0 0-7 7c0 5 7 11 7 11s7-6 7-11a7 7 0 0 0-7-7zm0 10a3 3 0 1 1 0-6 3 3 0 0 1 0 6z"/></svg>Sed ut perspiciatis unde omnis iste natus</div>
    <div class="row"><svg width="14" height="14" viewBox="0 0 14 14" fill="#fff"><path d="M3 0l3 3-2 2c1 2 3 4 5 5l2-2 3 3-2 3C6 14 0 8 0 2z"/></svg>Phone: +33 1 84 00 42 17</div>
    <div class="row"><svg width="16" height="12" viewBox="0 0 16 12" fill="none" stroke="#fff" stroke-width="1.6"><rect x="1" y="1" width="14" height="10"/><path d="M1 1l7 6 7-6"/></svg>contact@verdalis.org</div>
  </div>
  <div class="foot-col" style="left:985px">
    <h4>Follow Us</h4>
    <div class="row"><span class="sq"></span>Chatterly</div>
    <div class="row"><span class="sq"></span>Chirpnet</div>
  </div>
  <div class="copy">© 2024 Verdalis &nbsp;|&nbsp; All rights reserved.</div>
</footer>

</body>
</html>
```